Infographic - Engagement Survey

Infographic required to be used in our marketing collateral and our website

Target Market(s)

B2B - commercial, non for profit, private, government and council

Industry/Entity Type

Marketing

Font styles to use
Sans Serif

Colors
0455a3
3276b5
85abd2
cedeed
e34197

Requirements
Must have
• Please refer to document for branding colours, fonts used are arial, calibri and century gothic

```html
<!DOCTYPE html>
<html lang="en">
<head>
<meta charset="utf-8">
<title>Job, Team, Leader, and Organisation Factors Predicting Engagement</title>
<link href="https://fonts.googleapis.com/css2?family=Lato:wght@400;700;900&display=swap" rel="stylesheet">
<style>
  :root{
    --navy:#343d6a;
    --pink:#cc3596;
    --blue:#5b9ad2;
    --gold:#e4a42a;
    --pale:#eef1f9;
    --ink:#222222;
    --white:#ffffff;
  }
  *{margin:0;padding:0;box-sizing:border-box}
  html,body{width:957px;height:1200px;overflow:hidden;background:var(--white)}
  body{font-family:'Lato',Arial,sans-serif;color:var(--ink);position:relative}
  .abs{position:absolute}

  .header{left:0;top:0;width:957px;height:160px;background:var(--navy)}
  .header-title{left:37px;top:20px;color:var(--white);font-weight:900;font-size:39px;line-height:39px;letter-spacing:-0.3px}
  .brand{right:26px;top:58px;color:var(--white);font-weight:900;font-size:34px;line-height:40px;text-align:right}
  .stripe-pink{left:0;top:160px;width:957px;height:8px;background:var(--pink)}
  .stripe-blue{left:0;top:168px;width:957px;height:11px;background:var(--blue)}

  .measure{left:0;top:179px;width:957px;height:249px;background:var(--pale)}
  .measure-title{left:34px;top:110px;font-size:29px;font-weight:900;color:var(--ink)}
  .dimensions{left:542px;top:35px}

  .drivers{left:0;top:428px;width:957px;height:362px;background:var(--white)}
  .wheel{left:0;top:0}
  .factor-list{font-size:12px;line-height:15.4px;color:var(--ink);white-space:nowrap}
  .factor-list.right-align{text-align:right}

  .predictors{left:0;top:790px;width:957px;height:280px;background:var(--pale)}
  .predictors-title{left:0;width:957px;top:12px;text-align:center;font-size:28px;font-weight:900}
  .beta-head{top:46px;font-size:17px;font-weight:700}
  .beta-table{left:319px;top:72px;width:319px}
  .beta-row{height:22.8px;margin-bottom:0.5px;display:flex;justify-content:space-between;align-items:center;padding:0 6px 0 5px;color:var(--white);font-size:13.5px;border-bottom:1.5px solid var(--white);white-space:nowrap}
  .beta-row.job{background:var(--pink)}
  .beta-row.leader{background:var(--gold)}
  .beta-row.team{background:var(--navy)}

  .summary{left:0;top:1070px;width:957px;height:110px;background:var(--white)}
  .summary-title{left:18px;top:24px;font-size:28px;font-weight:900;line-height:35px}
  .summary-col{font-size:15px;text-align:center;line-height:17px;transform:translateX(-50%);white-space:nowrap}
  .summary-rule{left:428px;top:61px;width:510px;height:3px;background:var(--navy)}

  .foot-blue{left:0;top:1180px;width:957px;height:6px;background:var(--blue)}
  .foot-pink{left:0;top:1186px;width:957px;height:6px;background:var(--pink)}
  .foot-navy{left:0;top:1192px;width:957px;height:8px;background:var(--navy)}
</style>
</head>
<body>

<header class="header abs">
  <h1 class="header-title abs">Job, Team, Leader,<br>and Organisation Factors<br>Predicting Engagement</h1>
  <div class="brand abs">Norvale<br>Consulting</div>
</header>
<div class="stripe-pink abs"></div>
<div class="stripe-blue abs"></div>

<section class="measure abs">
  <h2 class="measure-title abs">How do we measure Engagement?</h2>
  <svg class="dimensions abs" width="380" height="190" viewBox="0 0 380 190">
    <g font-family="Lato, Arial, sans-serif" font-weight="900" fill="#fff" text-anchor="middle">
      <polygon points="0,62 61,0 122,62 122,186 61,130 0,186" fill="var(--pink)"/>
      <circle cx="61" cy="58" r="20" fill="#fff"/>
      <polygon points="64,44 52,61 60,61 56,73 70,54 62,54" fill="var(--pink)"/>
      <text x="61" y="113" font-size="27">ENERGY</text>

      <polygon points="127,62 188,0 249,62 249,186 188,130 127,186" fill="var(--blue)"/>
      <circle cx="188" cy="58" r="20" fill="#fff"/>
      <polyline points="178,58 185,65 199,50" fill="none" stroke="var(--blue)" stroke-width="5" stroke-linecap="round" stroke-linejoin="round"/>
      <text x="188" y="108" font-size="15.5">COMMITMENT</text>

      <polygon points="253,62 314,0 375,62 375,186 314,130 253,186" fill="var(--gold)"/>
      <circle cx="314" cy="58" r="20" fill="#fff"/>
      <path d="M303,54 q5.5,-5 11,0 t11,0 M303,62 q5.5,-5 11,0 t11,0" fill="none" stroke="var(--gold)" stroke-width="3" stroke-linecap="round"/>
      <text x="314" y="113" font-size="30">FLOW</text>
    </g>
  </svg>
</section>

<section class="drivers abs">
  <svg class="wheel abs" width="957" height="362" viewBox="0 428 957 362">
    <path d="M320.5,558.6 A214,214 0 0 1 498.3,458 L500.5,584 A88,88 0 0 0 427.4,625.4 Z" fill="var(--gold)"/>
    <path d="M505.7,458 A214,214 0 0 1 685.4,561.8 L577.4,626.7 A88,88 0 0 0 503.5,584 Z" fill="var(--pink)"/>
    <path d="M689.2,568.2 A214,214 0 0 1 689.2,775.8 L579,714.7 A88,88 0 0 0 579,629.3 Z" fill="var(--blue)"/>
    <path d="M314.8,775.8 A214,214 0 0 1 314.8,568.2 L425,629.3 A88,88 0 0 0 425,714.7 Z" fill="var(--navy)"/>

    <rect x="408" y="504" width="44" height="36" rx="6" fill="#fff" opacity="0.35" role="img" aria-label="Leader group icon"/>
    <g fill="#fff">
      <rect x="557" y="509" width="42" height="30" rx="3"/>
      <rect x="570" y="502" width="16" height="9" rx="2" fill="none" stroke="#fff" stroke-width="3"/>
      <rect x="557" y="521" width="42" height="2" fill="var(--pink)"/>
      <rect x="575" y="518" width="6" height="8" rx="1" fill="var(--pink)"/>
    </g>
    <rect x="338" y="632" width="40" height="40" rx="6" fill="#fff" opacity="0.35" role="img" aria-label="Team group icon"/>
    <g fill="#fff">
      <polygon points="630,628 652,620 664,626 664,676 630,676"/>
      <rect x="636" y="638" width="18" height="3" fill="var(--blue)"/>
      <rect x="636" y="646" width="18" height="3" fill="var(--blue)"/>
      <rect x="636" y="654" width="18" height="3" fill="var(--blue)"/>
      <rect x="636" y="662" width="18" height="3" fill="var(--blue)"/>
    </g>

    <g font-family="Lato, Arial, sans-serif" font-weight="900" fill="#fff" text-anchor="middle">
      <text x="430" y="571" font-size="19">LEADER</text>
      <text x="578" y="576" font-size="28">JOB</text>
      <text x="358" y="703" font-size="19">TEAM</text>
      <text x="650" y="705" font-size="15">ORGANISATION</text>
    </g>
    <g font-family="Lato, Arial, sans-serif" fill="var(--ink)" text-anchor="middle">
      <text x="502" y="668" font-size="19">What Affects</text>
      <text x="502" y="694" font-size="21" font-weight="900">ENGAGEMENT</text>
    </g>

    <g stroke-width="1.5">
      <line x1="278" y1="462" x2="278" y2="609" stroke="var(--gold)"/>
      <line x1="725" y1="466" x2="725" y2="530" stroke="var(--pink)"/>
      <line x1="727" y1="617" x2="727" y2="728" stroke="var(--blue)"/>
      <line x1="277" y1="649" x2="277" y2="719" stroke="var(--navy)"/>
    </g>
    <g fill="var(--gold)">
      <circle cx="278" cy="462" r="3.2"/><circle cx="278" cy="477.4" r="3.2"/><circle cx="278" cy="492.8" r="3.2"/><circle cx="278" cy="508.2" r="3.2"/><circle cx="278" cy="523.6" r="3.2"/><circle cx="278" cy="539" r="3.2"/><circle cx="278" cy="554.4" r="3.2"/><circle cx="278" cy="569.8" r="3.2"/><circle cx="278" cy="585.2" r="3.2"/><circle cx="278" cy="600.6" r="3.2"/>
    </g>
    <g fill="var(--pink)">
      <circle cx="725" cy="466" r="3.2"/><circle cx="725" cy="481.4" r="3.2"/><circle cx="725" cy="496.8" r="3.2"/><circle cx="725" cy="512.2" r="3.2"/><circle cx="725" cy="527.6" r="3.2"/>
    </g>
    <g fill="var(--blue)">
      <circle cx="727" cy="617" r="3.2"/><circle cx="727" cy="632.4" r="3.2"/><circle cx="727" cy="647.8" r="3.2"/><circle cx="727" cy="663.2" r="3.2"/><circle cx="727" cy="678.6" r="3.2"/><circle cx="727" cy="694" r="3.2"/><circle cx="727" cy="709.4" r="3.2"/><circle cx="727" cy="724.8" r="3.2"/>
    </g>
    <g fill="var(--navy)">
      <circle cx="277" cy="655" r="3.2"/><circle cx="277" cy="670.4" r="3.2"/><circle cx="277" cy="685.8" r="3.2"/><circle cx="277" cy="701.2" r="3.2"/><circle cx="277" cy="716.6" r="3.2"/>
    </g>
  </svg>

  <ul class="factor-list right-align abs" style="right:685px;top:27px;list-style:none">
    <li>Creates a learning environment</li>
    <li>Supportive Leadership</li>
    <li>Fosters teamwork</li>
    <li>Encourages autonomous decision making</li>
    <li>Creates clarity about appropriate behaviours</li>
    <li>Effective management of behaviours</li>
    <li>Creates clarity about performance standards</li>
    <li>Effective management of underperformance</li>
    <li>Celebrate success</li>
    <li>Optimism and positivity</li>
  </ul>
  <ul class="factor-list abs" style="left:733px;top:31px;list-style:none">
    <li>Optimism</li>
    <li>Variety of Work</li>
    <li>Self confidence</li>
    <li>Learning at work</li>
    <li>Knowledge of processes and policies</li>
  </ul>
  <ul class="factor-list abs" style="left:735px;top:182px;list-style:none">
    <li>Optimism</li>
    <li>Willingness to change</li>
    <li>Encouragesment and support</li>
    <li>Freedom to make decisions</li>
    <li>Recognition of performance</li>
    <li>Clarity of goals</li>
    <li>Customer commitment</li>
    <li>Performance feedback</li>
  </ul>
  <ul class="factor-list right-align abs" style="right:687px;top:220px;list-style:none">
    <li>Freedom to make decisions</li>
    <li>Optimism</li>
    <li>Customer Commitment</li>
    <li>Performance feedback</li>
    <li>Clarity of goals</li>
  </ul>
</section>

<section class="predictors abs">
  <h2 class="predictors-title abs">What are the best predictors of Engagement?</h2>
  <div class="beta-head abs" style="left:324px">Factor</div>
  <div class="beta-head abs" style="right:327px">Beta Weights</div>
  <div class="beta-table abs">
    <div class="beta-row job"><span>(CB) Learning at Work</span><span>.257</span></div>
    <div class="beta-row job"><span>(CB) Optimism - Job</span><span>.238</span></div>
    <div class="beta-row job"><span>(CB) Self Confidence</span><span>.207</span></div>
    <div class="beta-row job"><span>(CB) Variety of Work</span><span>.189</span></div>
    <div class="beta-row leader"><span>(LB) Creates a Learning Environment</span><span>-.131</span></div>
    <div class="beta-row team"><span>(CB) Optimism - Team</span><span>.123</span></div>
    <div class="beta-row team"><span>(CB) Clarity of Goals - Team</span><span>.112</span></div>
    <div class="beta-row team"><span>(CB) Recognition of Performance - Team</span><span>.103</span></div>
  </div>
</section>

<section class="summary abs">
  <h2 class="summary-title abs">Model<br>Summary</h2>
  <div class="summary-col abs" style="left:450px;top:40px">Model</div>
  <div class="summary-col abs" style="left:533px;top:40px">R</div>
  <div class="summary-col abs" style="left:626px;top:40px">R Square</div>
  <div class="summary-col abs" style="left:742px;top:23px">Adjusted<br>R Square</div>
  <div class="summary-col abs" style="left:886px;top:23px">STD Error of<br>the Estimate</div>
  <div class="summary-rule abs"></div>
  <div class="summary-col abs" style="left:450px;top:71px">1</div>
  <div class="summary-col abs" style="left:533px;top:71px">.806</div>
  <div class="summary-col abs" style="left:623px;top:71px">.650</div>
  <div class="summary-col abs" style="left:738px;top:71px">.641</div>
  <div class="summary-col abs" style="left:886px;top:71px">.64165</div>
</section>

<div class="foot-blue abs"></div>
<div class="foot-pink abs"></div>
<div class="foot-navy abs"></div>

</body>
</html>
```